Dental Business Card

I need Dental oriented business cards.
On the front side -
- on the first line, my name:
Dr Marlo Vintner
- on the second line (just underneath):
Doctor of Dental Medicine
- on the third line, or underneath that or in a corner, I would like the address and phone number:
5182 Ch. Birchfield
Montreal QC H2T 4B9
514-629-5074
- other than that i would maybe like a logo of a tooth, but i want it to be subtle and very basic!
- I would like the card to be preferably black or dark grey-ish with the writing in white
On the other side -
- 2-3 lines with the possibility to write the next appointment the box with the lines should be white, with the rest of the card being black

```html
<!DOCTYPE html>
<html lang="en">
<head>
<meta charset="utf-8">
<title>Dr Marlo Vintner – Business Card</title>
<link rel="stylesheet" href="https://fonts.googleapis.com/css2?family=Open+Sans:wght@400;600;700&display=swap">
<style>
  :root {
    --page-bg: #eef4ef;
    --card-bg: #1d1012;
    --mark-tone: #2a1d20;
    --ink: #ffffff;
    --ink-soft: #e6e2e3;
    --icon: #9a9496;
  }
  * { box-sizing: border-box; margin: 0; padding: 0; }
  html, body {
    width: 1200px; height: 800px; overflow: hidden;
    background: var(--page-bg);
    font-family: "Open Sans", Arial, sans-serif;
  }
  .canvas {
    position: relative; width: 1200px; height: 800px;
  }
  .card {
    position: absolute; top: 280px;
    width: 420px; height: 240px;
    background: var(--card-bg);
    color: var(--ink);
    overflow: hidden;
  }
  .card--back { left: 150px; }
  .card--front { left: 630px; }

  .tooth-mark {
    position: absolute; left: -10px; top: 22px;
    width: 170px; height: 200px;
    background: var(--mark-tone);
    border-radius: 70px 70px 40px 40px;
  }

  /* Back side */
  .appointment {
    position: absolute; right: 22px; top: 60px; width: 210px;
  }
  .appointment__title {
    font-size: 11px; font-weight: 400; text-align: right;
    margin-bottom: 8px;
  }
  .appointment__line {
    height: 2px; background: var(--ink); margin-bottom: 24px;
  }

  /* Front side */
  .identity {
    position: absolute; left: 242px; top: 38px;
  }
  .identity__name { font-size: 17px; font-weight: 700; line-height: 1.2; }
  .identity__title { font-size: 9.5px; color: var(--ink-soft); margin-top: 4px; }

  .contact {
    position: absolute; left: 224px; top: 146px;
    font-size: 11px; line-height: 16px; color: var(--ink-soft);
    list-style: none;
  }
  .contact__item { display: flex; align-items: flex-start; gap: 7px; }
  .contact__icon { width: 10px; height: 12px; margin-top: 2px; flex: none; }
</style>
</head>
<body>
<main class="canvas">

  <section class="card card--back" aria-label="Business card back">
    <div class="tooth-mark" role="img" aria-label="Subtle tooth logo mark"></div>
    <div class="appointment">
      <p class="appointment__title">Next Appointment</p>
      <div class="appointment__line"></div>
      <div class="appointment__line"></div>
      <div class="appointment__line"></div>
    </div>
  </section>

  <section class="card card--front" aria-label="Business card front">
    <div class="tooth-mark" role="img" aria-label="Subtle tooth logo mark"></div>
    <div class="identity">
      <h1 class="identity__name">Dr Marlo Vintner</h1>
      <p class="identity__title">Doctor of Dental Medicine</p>
    </div>
    <ul class="contact">
      <li class="contact__item">
        <svg class="contact__icon" viewBox="0 0 10 12" aria-hidden="true">
          <path d="M5 0.5a4 4 0 0 0-4 4c0 3 4 7 4 7s4-4 4-7a4 4 0 0 0-4-4z" fill="none" stroke="var(--icon)" stroke-width="1.2"/>
          <circle cx="5" cy="4.5" r="1.4" fill="var(--icon)"/>
        </svg>
        <span>5182 Ch. Birchfield<br>Montreal QC H2T 4B9</span>
      </li>
      <li class="contact__item">
        <svg class="contact__icon" viewBox="0 0 10 12" aria-hidden="true">
          <path d="M0.5 4.5c0-1.5 2-2.5 4.5-2.5s4.5 1 4.5 2.5v1h-2.5v-1.2h-4v1.2h-2.5z" fill="var(--icon)"/>
          <rect x="2" y="6.5" width="6" height="4" rx="0.8" fill="var(--icon)"/>
        </svg>
        <span>514-629-5074</span>
      </li>
    </ul>
  </section>

</main>
</body>
</html>
```